My company produces chocolate bars; currently have 4 bars that are packaged in slim window boxes.

I need some product images, but the photos we've taken look awful. I think someone with solid Photoshop skills could take our electronic files and create some product images based on the digital files.

I need 4 product images. Also, if you are able to product any additional general images like this:
http://quillmora.com/velnutrafanatic/treats-make-our-meadow-glow/

```html
<!DOCTYPE html>
<html lang="en">
<head>
<meta charset="utf-8">
<title>Marisette Cacao – Chili Pepper bar</title>
<link rel="stylesheet" href="https://fonts.googleapis.com/css2?family=Kalam:wght@400&family=Open+Sans:wght@400&display=swap">
<style>
  :root {
    --backdrop: #eeeeee;
    --box-black: #0b0b0b;
    --box-sheen: #2a2a2a;
    --band-red: #a30d0f;
    --band-red-deep: #7e0708;
    --ink-white: #f4f4f4;
    --ink-grey: #c9c9c9;
    --cocoa-dark: #1e0f0c;
    --cocoa-mid: #3b211c;
  }
  html, body {
    margin: 0;
    padding: 0;
    width: 1200px;
    height: 1000px;
    overflow: hidden;
    background: var(--backdrop);
  }
  .canvas {
    position: relative;
    width: 1200px;
    height: 1000px;
    background: var(--backdrop);
  }
  .bar-box {
    position: absolute;
    left: 320px;
    top: 60px;
    width: 560px;
    height: 880px;
    background: linear-gradient(160deg, var(--box-sheen) 0%, var(--box-black) 35%, var(--box-black) 100%);
    box-shadow: 0 18px 40px rgba(0,0,0,0.25);
    overflow: hidden;
  }
  .brand {
    position: absolute;
    top: 150px;
    left: 0;
    width: 100%;
    text-align: center;
    font-family: "Open Sans", sans-serif;
    font-weight: 400;
    color: var(--ink-white);
  }
  .brand-first {
    display: block;
    font-size: 26px;
    letter-spacing: 0.32em;
  }
  .brand-second {
    display: block;
    font-size: 64px;
    line-height: 1.1;
    letter-spacing: 0.04em;
  }
  .flavour-band {
    position: absolute;
    top: 350px;
    left: 0;
    width: 100%;
    height: 84px;
    background: linear-gradient(90deg, var(--band-red-deep) 0%, var(--band-red) 50%, var(--band-red-deep) 100%);
    display: flex;
    align-items: center;
    justify-content: center;
  }
  .flavour-name {
    font-family: "Kalam", cursive;
    font-size: 52px;
    color: var(--ink-white);
    letter-spacing: 0.03em;
    padding-top: 8px;
  }
  .flavour-note {
    position: absolute;
    top: 454px;
    left: 0;
    width: 100%;
    text-align: center;
    font-family: "Open Sans", sans-serif;
    font-size: 27px;
    line-height: 1.25;
    color: var(--ink-grey);
    margin: 0;
  }
  .window {
    position: absolute;
    top: 560px;
    left: 60px;
    width: 440px;
    height: 270px;
    background: radial-gradient(ellipse at 35% 30%, var(--cocoa-mid) 0%, var(--cocoa-dark) 75%);
  }
</style>
</head>
<body>
  <main class="canvas">
    <section class="bar-box">
      <h1 class="brand">
        <span class="brand-first">MARISETTE</span>
        <span class="brand-second">Cacao</span>
      </h1>
      <div class="flavour-band">
        <span class="flavour-name">Chili Pepper</span>
      </div>
      <p class="flavour-note">Spicy chili pepper with 58%<br>dark chocolate</p>
      <div class="window" role="img" aria-label="Window showing the dark chocolate bar segments inside the box"></div>
    </section>
  </main>
</body>
</html>
```